Flyer for promoting a hotel in the beach in miami for an event

We are are KT Harbor and have a resort at Miami, Hallandale Beach.
We need a triptych:
- With a lot of photos to show the clients the wonderful experience they can live with their families going on vacations to miami.
- We want the amenities and photos of the units to stand out.
I attached a document called Triptico that is a guide for you to know what we want, and another called . When you do your design you must know that:
- The text should be linked to each photo. All the photos are attached.
- There is freedom to play with the structure. I did an example, but PLEASE mix this up and do it less structured.
- You can feel free to add any other photos at the background, from the ones I sent or from other places. Like for example of a family.

Target Market(s)

Families who go to vacaton to have a great experience and memories. Targeted to people who love the beach and miami

Industry/Entity Type

Hotel

Font styles to use
Sans Serif

Colors
ec1f27
ffffff

Requirements
Must have
• The photos with numbers

```html
<!DOCTYPE html>
<html lang="en">
<head>
<meta charset="utf-8">
<title>KT Harbor – Premium Beach Club Trifold</title>
<link href="https://fonts.googleapis.com/css2?family=Roboto:wght@400;500;700&display=swap" rel="stylesheet">
<style>
  :root {
    --brand-red: #ec1f27;
    --deep-red: #b3121a;
    --white: #ffffff;
    --ink: #1d1d1d;
    --stage: #d9d9d9;
    --photo-border: #e2262d;
  }
  * { box-sizing: border-box; margin: 0; padding: 0; }
  html, body { width: 1200px; height: 900px; overflow: hidden; }
  body { background: var(--stage); font-family: "Roboto", Arial, sans-serif; color: var(--ink); }

  .trifold { position: absolute; left: 14px; top: 37px; width: 1172px; height: 826px; display: flex; }
  .panel { position: relative; height: 100%; }

  /* ---------- Units panel ---------- */
  .panel--units { width: 391px; background: var(--brand-red); }
  .panel--units .sheet {
    position: absolute; left: 17px; top: 17px; width: 357px; height: 793px;
    background: linear-gradient(90deg, #ffffff 55%, #f1f1f1 100%);
  }
  .unit-photo, .amenity-photo, .club-photo {
    position: absolute; border-radius: 50%; border: 1.5px solid var(--photo-border);
  }
  .unit-photo { left: 25px; width: 170px; height: 170px; }
  .unit-info { position: absolute; left: 210px; width: 156px; text-align: center; font-size: 10.5px; line-height: 13.4px; }
  .unit-info .rate-label { font-weight: 700; }
  .unit-info .rule { height: 1.5px; background: var(--brand-red); margin: 6px -12px 6px -14px; }
  .unit-info .unit-name { font-weight: 700; text-transform: uppercase; }

  /* ---------- Beach club panel ---------- */
  .panel--club { width: 390px; overflow: hidden; }
  .panel--club .backdrop {
    position: absolute; inset: 0;
    background:
      radial-gradient(ellipse at 50% 30%, #ec1f27 0%, #d61a22 45%, transparent 75%),
      linear-gradient(180deg, #e31d25 0%, #c0141c 45%, #8e0d13 75%, #b0121a 100%);
  }
  .club-title {
    position: absolute; top: 44px; left: 0; width: 100%; text-align: center;
    color: var(--white); font-weight: 700; font-size: 28px; letter-spacing: -0.2px;
  }
  .club-hero {
    position: absolute; left: 50px; top: 91px; width: 278px; height: 149px;
    border: 2px solid var(--white);
    background: linear-gradient(180deg, #3d6fd0 0%, #9cc0ea 45%, #f1ede6 55%, #c9c2b8 100%);
  }
  .club-text {
    position: absolute; left: 52px; top: 255px; width: 286px; text-align: center;
    color: var(--white); font-size: 13.4px; line-height: 16.8px;
  }
  .club-photo { width: 170px; height: 170px; left: 110px; border-color: var(--white); }
  .club-caption {
    position: absolute; left: 0; width: 100%; top: 540px; text-align: center;
    color: var(--white); font-size: 13.4px; line-height: 16.2px;
  }

  /* ---------- Amenities panel ---------- */
  .panel--amenities { width: 391px; background: var(--brand-red); }
  .panel--amenities .sheet {
    position: absolute; left: 17px; top: 17px; width: 358px; height: 793px; overflow: hidden;
    background: linear-gradient(160deg, #ffffff 0%, #e8e8e8 35%, #cfcfcf 55%, #f0f0f0 80%, #ffffff 100%);
  }
  .amenity-photo { width: 170px; height: 170px; left: 100px; }
  .amenity-rule { position: absolute; height: 1.5px; background: var(--brand-red); }
  .amenity-caption {
    position: absolute; text-align: center; font-size: 13.4px; line-height: 16.8px; color: var(--ink);
  }
</style>
</head>
<body>
<main class="trifold">

  <section class="panel panel--units">
    <div class="sheet">
      <div class="unit-photo" style="top:19px;background:linear-gradient(180deg,#e9e7e4 0%,#c9c5bf 45%,#ffffff 60%,#1f3f7a 80%,#8a8580 100%);" role="img" aria-label="Studio bedroom with two made beds and blue throws"></div>
      <div class="unit-info" style="top:43px;">
        <p class="rate-label">Starting From</p>
        <p>$ 119.00/DAY</p><p>$ 699.00/WEEK</p><p>$2,099.00/MONTH</p>
        <div class="rule"></div>
        <p class="unit-name">Studio/One Bathroom</p>
        <p>· Intracoastal Waterway View</p><p>· Accommodates: 2</p><p>· Maximum Capacity: 4</p>
      </div>

      <div class="unit-photo" style="top:207px;background:linear-gradient(135deg,#f2f1ef 0%,#d9d7d3 45%,#9c9994 70%,#5c5a57 100%);" role="img" aria-label="Modern white kitchen with stainless steel appliances"></div>
      <div class="unit-info" style="top:231px;">
        <p class="rate-label">Starting From</p>
        <p>$ 119.00/DAY</p><p>$ 699.00/WEEK</p><p>$2,099.00/MONTH</p>
        <div class="rule"></div>
        <p class="unit-name">One Bedroom/One Bath-room</p>
        <p>· Intracoastal Waterway View</p><p>· Accommodates: 2</p><p>· Maximum Capacity: 4</p>
      </div>

      <div class="unit-photo" style="top:395px;background:linear-gradient(135deg,#cfd8e0 0%,#22486e 40%,#b9b2a8 65%,#8a8379 100%);" role="img" aria-label="Living room with sectional sofa and blue feature wall"></div>
      <div class="unit-info" style="top:411px;">
        <p class="rate-label">Starting From</p>
        <p>$ 119.00/DAY</p><p>$ 699.00/WEEK</p><p>$2,099.00/MONTH</p>
        <div class="rule"></div>
        <p class="unit-name">2 Bedroom/ 2 Bathroom</p>
        <p>· Intracoastal Waterway View</p><p>· Accommodates: 2</p><p>· Maximum Capacity: 4</p>
      </div>

      <div class="unit-photo" style="top:583px;background:linear-gradient(180deg,#efeeec 0%,#d4d1cc 45%,#6b5a4c 60%,#d8d4cf 75%,#355a6e 100%);" role="img" aria-label="Master bedroom with king bed and wood headboard"></div>
      <div class="unit-info" style="top:607px;">
        <p class="rate-label">Starting From</p>
        <p>$ 119.00/DAY</p><p>$ 699.00/WEEK</p><p>$2,099.00/MONTH</p>
        <div class="rule"></div>
        <p class="unit-name">3 Bedroom/3 Bathroom</p>
        <p>· Intracoastal Waterway View</p><p>· Accommodates: 2</p><p>· Maximum Capacity: 4</p>
      </div>
    </div>
  </section>

  <section class="panel panel--club">
    <div class="backdrop" role="img" aria-label="Red-toned poolside deck with palm trees and lounge cushions"></div>
    <h1 class="club-title">Premium Beach Club</h1>
    <div class="club-hero" role="img" aria-label="Beach club building with palm trees under a blue sky"></div>
    <p class="club-text">Free access to the Seaward Beach Club (at the beach) where you can enjoy beach chairs, towels and umbrellas for no additional cost (subject to availability). It also provides cocktails, premium dishes and much more.</p>
    <div class="club-photo" style="top:353px;background:linear-gradient(160deg,#ffffff 0%,#e9eef2 35%,#4fb4e6 55%,#c23a3a 75%,#e8d9bf 100%);" role="img" aria-label="White beach umbrellas over rows of lounge chairs"></div>
    <p class="club-caption">Free Beach Club Access<br>and chairs just for you!</p>
    <div class="club-photo" style="top:588px;background:linear-gradient(180deg,#6d8fb8 0%,#d5dee8 35%,#7fc3c9 50%,#e6dccb 65%,#bfb29c 100%);" role="img" aria-label="Sandy beach with blue loungers and the ocean"></div>
  </section>

  <section class="panel panel--amenities">
    <div class="sheet" role="img" aria-label="Grayscale view of the resort pool deck and tower">
      <div class="amenity-photo" style="top:18px;background:linear-gradient(180deg,#4e8fd6 0%,#a8cdec 40%,#3f7f5a 60%,#c8c6c2 80%,#8f8c88 100%);" role="img" aria-label="Shuttle cart in front of the resort tower"></div>
      <div class="amenity-rule" style="top:199px;left:43px;width:285px;"></div>
      <p class="amenity-caption" style="top:207px;left:60px;width:250px;">One block ride to the beach, back and forth, every few minutes!</p>

      <div class="amenity-photo" style="top:270px;background:linear-gradient(180deg,#3f78c8 0%,#cfd6dc 35%,#f2f2f0 55%,#2ab0d8 75%,#8e8a84 100%);" role="img" aria-label="Infinity pool beside the resort tower"></div>
      <div class="amenity-rule" style="top:449px;left:48px;width:275px;"></div>
      <p class="amenity-caption" style="top:452px;left:40px;width:290px;">Infinity Pool by Marvello alongside the Intracoastal Waterway<br>- Chase Lounge - Towel Service</p>

      <div class="amenity-photo" style="top:522px;background:linear-gradient(180deg,#4f86cf 0%,#c9d4de 35%,#b8b2a7 55%,#e8c53a 75%,#2d4b5e 100%);" role="img" aria-label="Yellow water taxi docked by waterfront towers"></div>
      <div class="amenity-rule" style="top:701px;left:111px;width:149px;"></div>
      <p class="amenity-caption" style="top:708px;left:85px;width:200px;">Water Taxi Stop!</p>
    </div>
  </section>

</main>
</body>
</html>
```